Tarnby Group letterhead

Hi,

I need a letterhead template created for our business. This should be done in word format and A4 size. The images need to not move in the template ie when I am adding writing in etc. and should flow on when I get to a second page.

I have attached our logo templates below.

Other details to include on the letterhead somewhere are:

0438 915 267
Max@Tarnbyelectrical.example.au
PO Box 817 Marrowvale NSW 2190
ABN: 57 318 962 407

Thanks!

```html
<!DOCTYPE html>
<html lang="en">
<head>
<meta charset="utf-8">
<title>Tarnby Group Letterhead</title>
<link rel="stylesheet" href="https://fonts.googleapis.com/css2?family=Open+Sans:wght@400;700;800&family=Poppins:wght@400;500&display=swap">
<style>
  :root {
    --backdrop: #cfd4d4;
    --paper: #ffffff;
    --ink: #1c1c1c;
    --charcoal: #2f2f2f;
    --orange: #ef5223;
    --muted: #444444;
  }
  * { box-sizing: border-box; margin: 0; padding: 0; }
  html, body { width: 1200px; height: 686px; overflow: hidden; }
  body {
    background: var(--backdrop);
    font-family: "Open Sans", Arial, sans-serif;
    color: var(--ink);
    position: relative;
  }
  .letterhead {
    position: absolute;
    left: 370px; top: 18px;
    width: 460px; height: 650px;
    background: var(--paper);
    box-shadow: 0 6px 18px rgba(0,0,0,.18);
    overflow: hidden;
  }
  .header-rule, .footer-rule { position: absolute; left: 0; width: 100%; height: 10px; }
  .header-rule { top: 74px; }
  .brand {
    position: absolute; left: 40px; top: 34px;
    display: flex; align-items: center; gap: 8px;
  }
  .brand-dot { width: 22px; height: 22px; border-radius: 50%; background: var(--orange); }
  .brand-name { font-weight: 800; font-size: 15px; letter-spacing: .5px; color: var(--ink); text-transform: uppercase; }
  .content { position: absolute; left: 40px; top: 112px; width: 380px; font-size: 7.6px; line-height: 1.45; }
  .date { margin-bottom: 9px; }
  .recipient-name { font-weight: 800; font-size: 10.5px; line-height: 1.2; }
  .recipient-role { margin-bottom: 9px; }
  .recipient-address { margin-bottom: 18px; }
  .salutation { font-weight: 800; font-size: 11.5px; margin-bottom: 10px; }
  .paragraph { margin-bottom: 13px; }
  .signature-mark { width: 120px; height: 34px; margin: 14px 0 4px 50px; border-radius: 4px; background: linear-gradient(90deg, #f1f1f1, #e3e3e3); }
  .signer-name { font-weight: 800; font-size: 19px; line-height: 1.1; margin-left: 50px; }
  .signer-role { margin-left: 50px; font-size: 8px; }
  .footer-rule { top: 560px; }
  .contact-row {
    position: absolute; left: 0; top: 578px; width: 100%;
    display: flex; justify-content: space-between; padding: 0 22px;
    font-family: "Poppins", Arial, sans-serif; font-size: 7.4px; color: var(--ink);
  }
  .contact-item { display: flex; align-items: center; gap: 4px; }
  .contact-item svg { width: 8px; height: 8px; flex: none; }
  .contact-accent { color: var(--orange); }
  .abn { position: absolute; left: 0; top: 596px; width: 100%; text-align: center;
    font-family: "Poppins", Arial, sans-serif; font-size: 7.4px; color: var(--orange); }
  .footer-band { position: absolute; left: 0; bottom: 0; width: 100%; height: 26px; }
</style>
</head>
<body>
  <main class="letterhead">
    <svg class="header-rule" viewBox="0 0 460 10" preserveAspectRatio="none">
      <line x1="0" y1="5" x2="460" y2="5" stroke="var(--charcoal)" stroke-width="1"/>
      <line x1="20" y1="5" x2="210" y2="5" stroke="var(--orange)" stroke-width="2.5"/>
    </svg>
    <div class="brand">
      <span class="brand-dot"></span>
      <span class="brand-name">Tarnby Group</span>
    </div>

    <section class="content">
      <p class="date">August-05-2019</p>
      <p class="recipient-name">Elena Varga</p>
      <p class="recipient-role">Director</p>
      <p class="recipient-address">1840 Larkspur Ave. Suite 310<br>Fenwick, TX 75031</p>
      <p class="salutation">Elena Varga</p>
      <p class="paragraph">Lorem ipsum dolor sit amet, consectetuer adipiscing elit, sed diam nonummy nibh euismod tincid­unt ut laoreet dolore magna aliquam erat volutpat. Ut wisi enim ad minim veniam, quis nostrud exerci tation ullamcorper suscipit lobortis</p>
      <p class="paragraph">Lorem ipsum dolor sit amet, cons ectetuer adipiscing elit, sed diam nonummy nibh euismod tincid­unt ut laoreet dolore magna aliquam erat volutpat. Ut wisi enim ad minim veniam, quis nostrud exerci tation ullamcorper suscipit lobortis nisl ut aliquip ex ea commodo consequat. Lorem ipsum dolor sit amet, consectetuer olutpat. Ut wisi enim ad minim veniam, quis nostrud exerci tation ullam­corper suscipit lobortis nisl ut aliquip ex ea commodo consequat. Duis autem</p>
      <p class="paragraph">vel eum iriure dolor in hendrerit in vulputate velit esse molestie consequat, vel illum dolore eu feugiat nulla facilisis at vero eros et accumsan et iusto odio dignissim qui blandit praesent luptatum zzril delenit augue duis dolore te feugait nulla facilisi. Lorem ipsum dolor sit amet, cons ectetuer adipiscing elit, sed diam nonummy nibh euismod tincidunt ut laoreet dolore magna aliquam erat volutpat. Ut wisi enim .</p>
      <div class="signature-mark" role="img" aria-label="Handwritten signature of Jordan Pell"></div>
      <p class="signer-name">Jordan Pell</p>
      <p class="signer-role">Co-Founder</p>
    </section>

    <svg class="footer-rule" viewBox="0 0 460 10" preserveAspectRatio="none">
      <line x1="0" y1="5" x2="460" y2="5" stroke="var(--charcoal)" stroke-width="1"/>
      <line x1="120" y1="5" x2="340" y2="5" stroke="var(--orange)" stroke-width="2.5"/>
    </svg>

    <div class="contact-row">
      <span class="contact-item">
        <svg viewBox="0 0 10 10"><path d="M2 1l2 2-1 1.3c.6 1.2 1.5 2.1 2.7 2.7L7 6l2 2-1.2 1.5C4.5 9 1 5.5.5 2.2z" fill="var(--orange)"/></svg>
        0438 915 267
      </span>
      <span class="contact-item">
        <svg viewBox="0 0 10 10"><rect x=".5" y="2" width="9" height="6.5" rx="1" fill="var(--orange)"/><path d="M1 2.6l4 3 4-3" stroke="#fff" stroke-width=".9" fill="none"/></svg>
        Max@<span class="contact-accent">Tarnbyelectrical.example.au</span>
      </span>
      <span class="contact-item">
        <svg viewBox="0 0 10 10"><path d="M5 .5a3.3 3.3 0 0 1 3.3 3.3C8.3 6.3 5 9.5 5 9.5S1.7 6.3 1.7 3.8A3.3 3.3 0 0 1 5 .5z" fill="var(--orange)"/><circle cx="5" cy="3.8" r="1.2" fill="#fff"/></svg>
        PO Box 817 Marrowvale NSW 2190
      </span>
    </div>
    <p class="abn">ABN: 57 318 962 407</p>

    <svg class="footer-band" viewBox="0 0 460 26" preserveAspectRatio="none">
      <rect x="0" y="0" width="460" height="26" fill="var(--orange)"/>
      <polygon points="300,26 318,0 460,0 460,26" fill="var(--charcoal)"/>
      <polygon points="278,26 296,0 300,0 282,26" fill="var(--charcoal)"/>
      <polygon points="286,26 304,0 308,0 290,26" fill="#fff"/>
      <polygon points="294,26 312,0 315,0 297,26" fill="var(--orange)"/>
    </svg>
  </main>
</body>
</html>
```